Flyer marketing document - Korlin MVE Engineering

We need a more modern version of a marketing flyer/ brochures for our business and service offering. I would like an overall business brochure, plus potentially some examples of specific parts of the business. The brochure attached provides a fairly detailed overview of the business. We need to extract what the core offering is and have the ability to sell to the market this offering, around the innovative design, engineering and manufacture of the equipment we offer.

```html
<!DOCTYPE html>
<html lang="en">
<head>
<meta charset="utf-8">
<title>Korlin MVE Engineering – Brochure Spreads</title>
<link rel="stylesheet" href="https://fonts.googleapis.com/css2?family=Open+Sans:ital,wght@0,400;0,600;0,700;0,800;1,600&family=Montserrat:wght@600;800&display=swap">
<style>
  :root {
    --red: #a30b0c;
    --red-deep: #8c0607;
    --yellow: #f6c400;
    --paper: #ffffff;
    --ink: #3a3a3a;
    --board: #6e6e6e;
    --spine: rgba(0,0,0,.10);
  }
  * { box-sizing: border-box; margin: 0; padding: 0; }
  html, body { width: 1200px; height: 641px; overflow: hidden; }
  body {
    background: var(--board);
    font-family: "Open Sans", Arial, sans-serif;
    color: var(--ink);
    position: relative;
  }
  .spread {
    position: absolute;
    width: 377px;
    height: 268px;
    background: var(--paper);
    overflow: hidden;
    box-shadow: 0 3px 8px rgba(0,0,0,.45);
  }
  .spread::after {
    content: "";
    position: absolute;
    left: 176px; top: 0;
    width: 26px; height: 100%;
    background: linear-gradient(90deg, transparent, var(--spine) 48%, rgba(255,255,255,.15) 52%, transparent);
    pointer-events: none;
  }
  .shapes { position: absolute; inset: 0; width: 377px; height: 268px; }
  .abs { position: absolute; }

  .brand-badge {
    position: absolute;
    height: 18px;
    width: 112px;
    display: flex; align-items: center; gap: 3px;
    padding-left: 16px;
  }
  .brand-badge svg { position: absolute; inset: 0; width: 100%; height: 100%; }
  .brand-badge .mark {
    position: relative;
    width: 5px; height: 5px; border-radius: 50%;
    background: var(--red);
  }
  .brand-name {
    position: relative;
    font-family: "Open Sans", sans-serif;
    font-weight: 800;
    font-size: 5.6px;
    letter-spacing: .1px;
    color: var(--red);
    text-transform: uppercase;
    white-space: nowrap;
  }
  .brand-plain { position: absolute; display: flex; align-items: center; gap: 3px; }
  .brand-plain .mark { width: 5px; height: 5px; border-radius: 50%; background: var(--red); }

  .site {
    position: absolute;
    font-size: 6px;
    color: #fff;
    bottom: 4px;
    letter-spacing: .1px;
  }
  .site.left { left: 15px; }
  .site.right { right: 14px; }

  .photo {
    position: absolute;
    border: 1.5px solid var(--yellow);
    border-radius: 3px;
    box-shadow: 1px 2px 3px rgba(0,0,0,.35);
  }
  .photo.bare { border: none; border-radius: 0; box-shadow: none; }
  .tone-yellow { background: linear-gradient(180deg, #a9c9e6 0%, #cdd9df 28%, #e0b423 40%, #c99a12 62%, #5c5246 84%, #8a7c66 100%); }
  .tone-orange { background: linear-gradient(180deg, #9fc1df 0%, #c7d4da 30%, #e0541e 46%, #b6380f 68%, #4d4540 86%, #8d8174 100%); }
  .tone-steel { background: linear-gradient(160deg, #d9a81a 0%, #8a7a5a 35%, #5f6468 60%, #c9c2b4 100%); }
  .tone-dirt { background: linear-gradient(180deg, #7ba4d1 0%, #c6b08a 35%, #e3b021 55%, #b77f3b 80%, #a86a3c 100%); }

  .body-text {
    position: absolute;
    font-size: 3.9px;
    line-height: 4.6px;
    color: var(--ink);
  }
  .body-text.justify { text-align: justify; }
  .body-text p + p { text-indent: 6px; }

  /* cover */
  .quote-mark {
    position: absolute;
    font-family: Georgia, "Times New Roman", serif;
    font-weight: 700;
    font-size: 34px;
    line-height: 1;
    color: var(--red);
  }
  .cover-title {
    position: absolute;
    left: 250px; top: 172px;
    font-family: "Montserrat", sans-serif;
    font-weight: 800;
    font-size: 8.6px;
    line-height: 9.2px;
    color: var(--red);
    text-transform: uppercase;
  }
  .cover-title .grey { color: #3a3a3a; font-weight: 600; }
  .contacts {
    position: absolute;
    font-size: 3.6px;
    line-height: 4.6px;
    color: var(--red);
    display: flex; gap: 10px;
  }

  .about-title {
    position: absolute;
    left: 14px; top: 84px;
    font-family: "Montserrat", sans-serif;
    font-weight: 800;
    font-size: 11px;
    line-height: 11.5px;
    color: #fff;
  }
  .italic-white {
    position: absolute;
    font-style: italic;
    font-weight: 600;
    font-size: 3.7px;
    line-height: 9px;
    color: #fff;
  }
  .photo-caption {
    position: absolute;
    left: 2px; top: 1px;
    font-size: 4.4px;
    font-weight: 600;
    color: #111;
  }
  .yellow-band-text {
    position: absolute;
    font-size: 4.2px;
    line-height: 5.3px;
    color: var(--red-deep);
  }
</style>
</head>
<body>

<!-- Spread 1: cover -->
<section class="spread" style="left:24px; top:79px;">
  <svg class="shapes" viewBox="0 0 377 268" aria-hidden="true">
    <polygon points="29,0 171,0 160,19 40,19" fill="var(--red)"/>
    <path d="M189,0 H262 V168 C300,160 340,175 377,200 V0 Z" fill="var(--red)"/>
    <path d="M189,0 C215,2 238,25 241,60 V168 C220,190 200,205 189,212 Z" fill="var(--red)"/>
    <rect x="189" y="172" width="52" height="38" fill="var(--red)"/>
    <rect x="0" y="257" width="377" height="11" fill="var(--red)"/>
  </svg>
  <div class="photo bare tone-yellow" role="img" aria-label="Mining water tanker with service platform parked in a yard"
       style="left:241px; top:0; width:136px; height:168px; border-top-left-radius:26px; border-bottom-right-radius:60px 24px;"></div>

  <span class="quote-mark" style="left:28px; top:80px;">“</span>
  <p class="body-text" style="left:50px; top:87px; width:108px; text-align:center; font-size:4.2px; line-height:5.2px;">
    Our design office uses the latest 3D CAD software for every project, ensuring fast and accurate design that moves quickly from concept to completion.
    Few engineering workshops in Australia can match our experience base, with 65 years of engineering and manufacturing experience, our delivery times and our competitive pricing.
  </p>
  <span class="quote-mark" style="left:157px; top:128px;">”</span>

  <div class="brand-plain" style="left:56px; top:219px;">
    <span class="mark"></span><span class="brand-name">Korlin MVE Engineering</span>
  </div>
  <div class="contacts" style="left:16px; top:239px;">
    <div>Western Australia Phone +61 400 555 218<br>Kai +61 400 555 309<br>Web: www.korlinmveengineering.com</div>
    <div>Email : office@korlinmveengineering.com<br>Email : kai@korlinmveengineering.com<br>Email : sales@korlinmveengineering.com</div>
  </div>

  <h1 class="cover-title"><span class="grey">Additional</span><br>Service Modules<br>and Water Tankers<br><span class="grey">for any vehicles</span></h1>

  <div class="brand-plain" style="left:199px; top:219px;">
    <span class="mark"></span><span class="brand-name">Korlin MVE Engineering</span>
  </div>
  <div class="contacts" style="left:202px; top:238px;">
    <div>Western Australia Phone +61 400 555 218<br>Kai +61 400 555 309<br>Web: www.korlinmveengineering.com</div>
    <div>Email : office@korlinmveengineering.com<br>Email : kai@korlinmveengineering.com<br>Email : sales@korlinmveengineering.com</div>
  </div>
</section>

<!-- Spread 2: about -->
<section class="spread" style="left:412px; top:79px;">
  <div class="photo bare tone-yellow" role="img" aria-label="Yellow articulated water tanker in a depot"
       style="left:143px; top:0; width:234px; height:118px;"></div>
  <svg class="shapes" viewBox="0 0 377 268" aria-hidden="true">
    <path d="M0,0 H188 L112,106 C105,114 96,118 84,118 H0 Z" fill="var(--red)"/>
    <path d="M188,0 H190 L143,118 H112 Z" fill="var(--paper)" opacity="0"/>
    <path d="M0,251 H120 L130,261 H280 L292,251 H377 V268 H0 Z" fill="var(--red)"/>
  </svg>
  <div class="brand-badge" style="left:0; top:17px;">
    <svg viewBox="0 0 112 18" preserveAspectRatio="none" aria-hidden="true"><polygon points="0,0 100,0 112,18 0,18" fill="var(--yellow)"/></svg>
    <span class="mark"></span><span class="brand-name">Korlin MVE Engineering</span>
  </div>
  <h2 class="about-title">About<br>Our Company</h2>
  <div class="body-text justify" style="left:15px; top:122px; width:157px;">
    <p>Formerly a local mining fabrication shop founded in 2009, the business began as a partnership between two engineering families with long careers in heavy equipment. Together they bring 67 years of experience in the design and fabrication of mining equipment, from water tanks and service trucks to tyre handlers and mobile cranes for on and off road use.</p>
    <p>They are committed to the highest quality products, service and support. A large network of suppliers lets them offer competitively priced products, reliable deliveries and the latest innovations.</p>
    <p>Since 2010, over 100 water tanks mainly for articulated dump trucks have rolled out of the home workshop, with tanks from 10,000 to 108,000 litres, some exported overseas for gold mining operations on an island mine.</p>
    <p>A simple but highly reliable engineering approach gives clients maximum machine availability and minimum downtime when repairs are needed. With 24 hour support and the ability to travel, customer support is second to none.</p>
  </div>
  <div class="photo tone-yellow" role="img" aria-label="Water tanker with platform, rear three-quarter view" style="left:203px; top:122px; width:77px; height:58px;"></div>
  <div class="photo tone-orange" role="img" aria-label="Red articulated tanker truck on a yard" style="left:284px; top:122px; width:77px; height:58px;"></div>
  <p class="body-text" style="left:203px; top:194px; width:158px; text-align:center;">
    Korlin MVE Engineering builds the best articulated dump truck water tankers and service trucks. Only the most reliable components go into our equipment to give the best possible availability of the finished product. The look, finish and quality of our products are second to none, and we offer our clients the very best in value for money.
  </p>
  <span class="site left">korlinmveengineering.com</span>
  <span class="site right">korlinmveengineering.com</span>
</section>

<!-- Spread 3: statement -->
<section class="spread" style="left:800px; top:79px;">
  <svg class="shapes" viewBox="0 0 377 268" aria-hidden="true">
    <path d="M0,0 H137 L188,88 L137,190 H0 Z" fill="var(--red)"/>
    <polygon points="120,140 150,140 220,262 80,262" fill="var(--yellow)"/>
    <path d="M0,251 H120 L130,261 H280 L292,251 H377 V268 H0 Z" fill="var(--red)"/>
  </svg>
  <div class="brand-badge" style="left:0; top:17px;">
    <svg viewBox="0 0 112 18" preserveAspectRatio="none" aria-hidden="true"><polygon points="0,0 100,0 112,18 0,18" fill="var(--yellow)"/></svg>
    <span class="mark"></span><span class="brand-name">Korlin MVE Engineering</span>
  </div>
  <p class="italic-white" style="left:16px; top:61px; width:150px;">
    There is no better designed or manufactured ADT water tank on the market.
    With the lowest centre of gravity, custom designed hydraulic, pneumatic
    systems and high quality paint finish, our clients know they can rely on getting
    the maximum return on their investment. Between 2011 and 2013 we have
    manufactured over 80 units on all leading articulated
    dump truck brands. We offer a complete turnkey service; all we need from the client is
    the truck and we handle the rest.
  </p>
  <div class="photo bare tone-yellow" role="img" aria-label="Large mining truck fitted with service deck and water tank"
       style="left:0; top:140px; width:220px; height:112px; clip-path:polygon(0 10%, 100% 0, 100% 100%, 0 100%);"></div>
  <div class="photo tone-yellow" role="img" aria-label="40 tonne class ADT water tanker beside a brick wall" style="left:210px; top:29px; width:150px; height:90px;">
    <span class="photo-caption">40 t class ADT water tanker, 35000 Lts</span>
  </div>
  <div class="photo tone-steel" role="img" aria-label="Tank access ladder and platform" style="left:210px; top:128px; width:103px; height:72px;"></div>
  <div class="photo tone-steel" role="img" aria-label="Close view of a control panel" style="left:287px; top:186px; width:73px; height:54px;"></div>
  <span class="site left">korlinmveengineering.com</span>
  <span class="site right">korlinmveengineering.com</span>
</section>

<!-- Spread 4: tanks -->
<section class="spread" style="left:24px; top:359px;">
  <svg class="shapes" viewBox="0 0 377 268" aria-hidden="true">
    <path d="M0,0 H150 L120,40 H0 Z" fill="var(--red)"/>
    <polygon points="30,142 188,142 188,175 52,175" fill="var(--yellow)"/>
    <path d="M0,251 H120 L130,261 H280 L292,251 H377 V268 H0 Z" fill="var(--red)"/>
  </svg>
  <div class="brand-badge" style="left:0; top:19px;">
    <svg viewBox="0 0 112 18" preserveAspectRatio="none" aria-hidden="true"><polygon points="0,0 100,0 112,18 0,18" fill="var(--yellow)"/></svg>
    <span class="mark"></span><span class="brand-name">Korlin MVE Engineering</span>
  </div>
  <div class="photo bare tone-yellow" role="img" aria-label="Yellow articulated water tanker, side view"
       style="left:15px; top:52px; width:173px; height:90px; clip-path:polygon(30% 0, 100% 0, 100% 100%, 0 100%);"></div>
  <p class="yellow-band-text" style="left:56px; top:146px; width:128px;">
    Service trucks use reliable and successful layouts for the product tanks and dispensing equipment. High flow diesel pumps have NMI compliant metering and recording equipment. Simple to use and designed for maximum reliability.
  </p>
  <div class="photo tone-steel" role="img" aria-label="Tank hatches seen from above" style="left:14px; top:180px; width:74px; height:60px;"></div>
  <div class="photo tone-yellow" role="img" aria-label="Spray cannon mounted on tank" style="left:98px; top:180px; width:77px; height:60px;"></div>

  <div class="photo tone-yellow" role="img" aria-label="Rigid water tank with safety access platform" style="left:207px; top:20px; width:72px; height:65px;"></div>
  <p class="body-text" style="left:290px; top:20px; width:72px;">
    Rigid water tanks with safety access platform for easy and safe maintenance of the water tanker pumping, spray systems and electrical systems. Tank fully raise-able using the existing hoist system integrated with water tank operating.
  </p>
  <p class="body-text" style="left:207px; top:111px; width:73px;">
    All tanks come with basic spray equipment or dust suppression and ground speed spray and spot spray water truck systems.
  </p>
  <div class="photo tone-yellow" role="img" aria-label="Rear of a rigid water tank truck" style="left:287px; top:78px; width:73px; height:62px;"></div>
  <div class="photo tone-steel" role="img" aria-label="Hydraulic manifolds and filters" style="left:207px; top:147px; width:72px; height:54px;"></div>
  <div class="photo tone-steel" role="img" aria-label="Control valve panel with gauges" style="left:287px; top:147px; width:73px; height:54px;"></div>
  <p class="body-text" style="left:207px; top:209px; width:155px;">
    Hydraulic systems use return filters and specially designed manifolds and control valving to simplify machine circuitry and the changes needed to allow its use as a water tanker. 30 years of experience modifying earthmoving equipment for water tankers and tool carriers is fully used to find the best modification procedure for each machine.
  </p>
  <span class="site left">korlinmveengineering.com</span>
  <span class="site right">korlinmveengineering.com</span>
</section>

<!-- Spread 5: service trucks -->
<section class="spread" style="left:412px; top:359px;">
  <svg class="shapes" viewBox="0 0 377 268" aria-hidden="true">
    <path d="M0,0 H40 L28,18 Q20,30 24,42 Z" fill="var(--red)"/>
    <polygon points="0,0 60,0 22,40 0,18" fill="var(--red)"/>
    <polygon points="293,0 310,0 335,30 325,34" fill="var(--yellow)"/>
    <path d="M0,251 H120 L130,261 H280 L292,251 H377 V268 H0 Z" fill="var(--red)"/>
  </svg>
  <p class="body-text" style="left:16px; top:52px; width:70px;">
    Service trucks use reliable and successful layouts for the product tanks and dispensing equipment. High flow diesel pumps have NMI compliant metering and recording equipment. Simple to use and designed for maximum reliability.
  </p>
  <div class="photo tone-orange" role="img" aria-label="Service module with open cabinets and reels" style="left:90px; top:37px; width:84px; height:60px;"></div>
  <div class="photo tone-orange" role="img" aria-label="Red tanker truck on a road" style="left:16px; top:102px; width:72px; height:56px;"></div>
  <p class="body-text" style="left:96px; top:128px; width:76px;">
    Unlike some of our competitors, our ADT tank layouts allow the use of standard wheel base trucks and maximise each truck's carrying capacity.
  </p>
  <div class="photo tone-steel" role="img" aria-label="Compressor bay inside a service module" style="left:16px; top:163px; width:72px; height:55px;"></div>
  <div class="photo tone-steel" role="img" aria-label="Gauge and switch control panel" style="left:95px; top:163px; width:71px; height:55px;"></div>
  <p class="body-text" style="left:16px; top:225px; width:155px;">
    We use a hydraulic drive screw air compressor with air capacity up to 165 cfm. Low maintenance with no diesel drive engine to service or "rattle apart". Hydraulic control systems allow the outputs of the fuel and pneumatic systems to be varied as required.
  </p>

  <p class="body-text" style="left:208px; top:60px; width:66px;">
    Proven tank design and cabinet layouts, with transport issues and sizing handled at the design stage, reduce the costs of moving plant around the country.
  </p>
  <div class="photo tone-yellow" role="img" aria-label="Service deck on a large haul truck" style="left:280px; top:37px; width:82px; height:61px;"></div>
  <div class="photo tone-yellow" role="img" aria-label="Tank mounting detail on truck chassis" style="left:208px; top:103px; width:82px; height:60px;"></div>
  <p class="body-text" style="left:295px; top:118px; width:68px;">
    Our in house design team ensures all possible options and client requirements are considered and built into the project. 30 years of design experience ensures only the best solutions are put forward and incorporated.
  </p>
  <p class="body-text" style="left:208px; top:205px; width:66px;">
    Large access areas with properly designed steps and platforms give the best maintenance opportunity.
  </p>
  <div class="photo tone-yellow" role="img" aria-label="Front view of truck with access steps" style="left:280px; top:170px; width:82px; height:60px;"></div>
  <span class="site left">korlinmveengineering.com</span>
  <span class="site right">korlinmveengineering.com</span>
</section>

<!-- Spread 6: gallery -->
<section class="spread" style="left:800px; top:359px;">
  <svg class="shapes" viewBox="0 0 377 268" aria-hidden="true">
    <path d="M0,0 H150 L120,40 H0 Z" fill="var(--red)"/>
    <path d="M0,251 H120 L130,261 H280 L292,251 H377 V268 H0 Z" fill="var(--red)"/>
  </svg>
  <div class="brand-badge" style="left:0; top:19px;">
    <svg viewBox="0 0 112 18" preserveAspectRatio="none" aria-hidden="true"><polygon points="0,0 100,0 112,18 0,18" fill="var(--yellow)"/></svg>
    <span class="mark"></span><span class="brand-name">Korlin MVE Engineering</span>
  </div>
  <div class="photo tone-orange" role="img" aria-label="Service module cabinet with hose reels" style="left:17px; top:59px; width:77px; height:66px;"></div>
  <div class="photo tone-orange" role="img" aria-label="Orange articulated tanker on site" style="left:98px; top:97px; width:76px; height:64px;"></div>
  <div class="photo tone-yellow" role="img" aria-label="Rear of yellow water tanker" style="left:17px; top:139px; width:77px; height:64px;"></div>
  <div class="photo tone-dirt" role="img" aria-label="Haul truck with water tank at mine site" style="left:98px; top:176px; width:76px; height:64px;"></div>
  <div class="photo tone-dirt" role="img" aria-label="Yellow tanker with awning on red dirt" style="left:207px; top:21px; width:148px; height:73px;"></div>
  <div class="photo tone-yellow" role="img" aria-label="Articulated tanker in a yard" style="left:207px; top:100px; width:72px; height:62px;"></div>
  <div class="photo tone-orange" role="img" aria-label="Orange tank module in workshop" style="left:286px; top:100px; width:69px; height:62px;"></div>
  <div class="photo tone-dirt" role="img" aria-label="Water truck beside an excavator at a mine" style="left:207px; top:168px; width:148px; height:72px;"></div>
  <span class="site left">korlinmveengineering.com</span>
  <span class="site right">korlinmveengineering.com</span>
</section>

</body>
</html>
```